Horse Brush Package design -

I need a design for a box - required for a rubber horse brush used for grooming and removing excess hair. The Brand is 'Maple Ridge Equestrian' and we develop top quality horse products. The design should be classy and professional

Box size is 21.5cm Length * 2cm high * 5 cm wide
Photo of logo and brush attached.
Box needs to have logo and description on front
Barcode on back.
Additional designs and photos can be added as you see fit.

"Horse Deshedding & Grooming Brush"
Brush away excess coat and dander
Gently remove dirt and mud
Soft, flexible design to gently groom around legs, ears and face.
Used when washing gives a deep clean to remove dirt
Gentle massage for increasing circulation
Durable, gentle, and kind to the horse

Target Market(s)

Horse Owners

Requirements
Must have
• Logo on the front, space for barcode on the back
Nice to have
• A nice horse photo would be suitable

```html
<!DOCTYPE html>
<html lang="en">
<head>
<meta charset="utf-8">
<title>Maple Ridge Equestrian – Deshedding Brush Box Dieline</title>
<link href="https://fonts.googleapis.com/css2?family=Roboto:ital,wght@0,900;1,900&family=Roboto+Condensed:wght@400;500&display=swap" rel="stylesheet">
<style>
  :root{
    --stage:#dcdcdf;
    --gold-dark:#b98420;
    --gold:#d7a540;
    --gold-light:#f0cd78;
    --ink:#111111;
    --paper:#ffffff;
    --line:#2a2a2a;
    --photo-dark:#1a1a1a;
    --photo-mid:#4a4a4a;
  }
  *{box-sizing:border-box;margin:0;padding:0}
  html,body{width:1200px;height:800px;overflow:hidden;background:var(--stage)}
  .canvas{position:relative;width:1200px;height:800px}
  .dieline{position:absolute;left:435px;top:15px;width:330px;height:770px}
  .dieline svg.cut{position:absolute;left:0;top:0}
  .panel{position:absolute;top:154px;height:462px;overflow:hidden}
  .panel--side-a{left:0;width:44px}
  .panel--front{left:44px;width:110px}
  .panel--side-b{left:154px;width:44px}
  .panel--back{left:198px;width:112px}
  .panel svg{position:absolute;left:0;top:0}

  .brand{position:absolute;left:6px;right:6px;top:30px;text-align:center;
    font-family:"Roboto Condensed",sans-serif;font-weight:500;color:var(--ink);
    font-size:9px;line-height:1.15;letter-spacing:.04em;text-transform:uppercase}
  .title{position:absolute;left:0;right:0;top:88px;text-align:center;color:var(--ink);
    font-family:"Roboto",sans-serif;font-weight:900;font-style:italic;font-size:12.5px;line-height:14px}
  .title .title__main{display:block;font-style:normal;font-size:25px;line-height:26px;margin-top:2px}

  .photo{position:absolute}
  .photo--horse{left:22px;top:158px;width:88px;height:130px;border-radius:40% 0 0 10%;
    background:radial-gradient(circle at 60% 40%,var(--photo-mid),var(--photo-dark) 70%)}
  .photo--brush{left:12px;top:254px;width:62px;height:112px;border-radius:8px;
    background:linear-gradient(100deg,#0d0d0d,#555 45%,#151515)}
  .panel--back .photo--brush{top:254px;height:96px;left:16px;width:58px}

  .tagline{position:absolute;left:0;right:0;top:374px;text-align:center;color:var(--ink);
    font-family:"Roboto Condensed",sans-serif;font-weight:500;font-size:12.5px;line-height:15px}
  .strip{position:absolute;left:0;right:0;top:406px;height:56px;background:var(--ink);color:var(--paper);
    font-family:"Roboto Condensed",sans-serif;font-size:6.6px;line-height:9px;text-align:center;padding:4px 6px 0}
  .back-copy{position:absolute;left:6px;right:6px;top:356px;text-align:center;color:var(--ink);
    font-family:"Roboto Condensed",sans-serif;font-size:6.6px;line-height:9px}
  .barcode-space{position:absolute;left:9px;width:94px;top:406px;height:50px;background:var(--ink);
    color:var(--paper);display:flex;align-items:center;justify-content:center;
    font-family:"Roboto Condensed",sans-serif;font-weight:500;font-size:13px}

  .spine{position:absolute;left:50%;width:110px;transform:translateX(-50%) rotate(-90deg);
    text-align:center;color:var(--ink);font-family:"Roboto",sans-serif;font-weight:900;font-style:italic;
    font-size:7.5px;line-height:9px}
  .spine--top{top:101px}
  .spine--bottom{top:315px;font-family:"Roboto Condensed",sans-serif;font-style:normal;font-weight:500;font-size:8px}
  .spine-brand{position:absolute;left:50%;top:219px;width:100px;transform:translateX(-50%) rotate(-90deg);
    text-align:center;color:var(--gold);font-family:"Roboto Condensed",sans-serif;font-weight:500;
    font-size:8px;line-height:9px;letter-spacing:.04em;text-transform:uppercase}
</style>
</head>
<body>
<div class="canvas">
  <div class="dieline">
    <svg class="cut" width="330" height="770" viewBox="0 0 330 770">
      <defs>
        <radialGradient id="flapGold" cx="50%" cy="35%" r="70%">
          <stop offset="0" stop-color="#f0cd78"/>
          <stop offset=".6" stop-color="#d7a540"/>
          <stop offset="1" stop-color="#b98420"/>
        </radialGradient>
      </defs>
      <path d="M44 154 V24 Q44 0 68 0 H130 Q154 0 154 24 V154 Z" fill="url(#flapGold)" stroke="#2a2a2a" stroke-width="1"/>
      <line x1="44" y1="42" x2="154" y2="42" stroke="#2a2a2a" stroke-width="1"/>
      <path d="M0 154 V116 L6 108 H38 L44 116 V154 Z" fill="url(#flapGold)" stroke="#2a2a2a" stroke-width="1"/>
      <path d="M154 154 V137 L160 129 H192 L198 137 V154 Z" fill="url(#flapGold)" stroke="#2a2a2a" stroke-width="1"/>
      <rect x="310" y="154" width="19.5" height="462" fill="#ffffff" stroke="#2a2a2a" stroke-width="1"/>
      <path d="M0 616 V634 L6 641 H38 L44 634 V616 Z" fill="url(#flapGold)" stroke="#2a2a2a" stroke-width="1"/>
      <path d="M154 616 V655 L160 663 H192 L198 655 V616 Z" fill="url(#flapGold)" stroke="#2a2a2a" stroke-width="1"/>
      <path d="M198 616 V746 Q198 770 222 770 H286 Q310 770 310 746 V616 Z" fill="url(#flapGold)" stroke="#2a2a2a" stroke-width="1"/>
      <line x1="198" y1="728" x2="310" y2="728" stroke="#2a2a2a" stroke-width="1"/>
      <rect x="0.5" y="154" width="309.5" height="462" fill="#ffffff" stroke="#2a2a2a" stroke-width="1"/>
    </svg>

    <section class="panel panel--side-a">
      <svg width="44" height="462" viewBox="0 0 44 462">
        <path d="M0 74 Q22 64 44 72 V170 Q22 178 0 168 Z" fill="var(--gold)"/>
        <path d="M0 290 Q22 280 44 288 V380 Q22 388 0 378 Z" fill="var(--gold)"/>
      </svg>
      <p class="spine spine--top">Horse Deshedding<br>&amp; Grooming Brush</p>
      <p class="spine-brand">Maple Ridge<br>Equestrian</p>
      <p class="spine spine--bottom">Brush Away Excess<br>Coat and Dander</p>
    </section>

    <section class="panel panel--front">
      <svg width="110" height="462" viewBox="0 0 110 462">
        <path d="M0 72 Q55 56 110 70 V292 Q55 276 0 296 Z" fill="var(--gold)"/>
        <path d="M0 68 Q55 52 110 66" fill="none" stroke="var(--gold)" stroke-width="1.5"/>
      </svg>
      <p class="brand">Maple Ridge<br>Equestrian</p>
      <h1 class="title">Horse<br>Deshedding<br>&amp; Grooming<span class="title__main">BRUSH</span></h1>
      <div class="photo photo--horse" role="img" aria-label="Photo of a black horse's head with flowing mane"></div>
      <div class="photo photo--brush" role="img" aria-label="Photo of the black rubber grooming brush, top and underside"></div>
      <p class="tagline">Brush Away Excess<br>Coat and Dander</p>
      <p class="strip">Gently remove dirt and mud Soft, flexible design to gently groom around legs, ears and face.</p>
    </section>

    <section class="panel panel--side-b">
      <svg width="44" height="462" viewBox="0 0 44 462">
        <path d="M0 74 Q22 64 44 72 V170 Q22 178 0 168 Z" fill="var(--gold)"/>
        <path d="M0 290 Q22 280 44 288 V380 Q22 388 0 378 Z" fill="var(--gold)"/>
      </svg>
      <p class="spine spine--top">Horse Deshedding<br>&amp; Grooming Brush</p>
      <p class="spine-brand">Maple Ridge<br>Equestrian</p>
      <p class="spine spine--bottom">Brush Away Excess<br>Coat and Dander</p>
    </section>

    <section class="panel panel--back">
      <svg width="112" height="462" viewBox="0 0 112 462">
        <path d="M0 72 Q56 56 112 70 V292 Q56 276 0 296 Z" fill="var(--gold)"/>
        <path d="M0 68 Q56 52 112 66" fill="none" stroke="var(--gold)" stroke-width="1.5"/>
      </svg>
      <p class="brand">Maple Ridge<br>Equestrian</p>
      <h2 class="title">Horse<br>Deshedding<br>&amp; Grooming<span class="title__main">BRUSH</span></h2>
      <div class="photo photo--horse" role="img" aria-label="Photo of a black horse's head with flowing mane"></div>
      <div class="photo photo--brush" role="img" aria-label="Photo of the black rubber grooming brush, top and underside"></div>
      <p class="back-copy">Used when washing gives a deep clean to remove dirt Gentle massage for increasing circulation Durable, gentle, and kind to the horse</p>
      <div class="barcode-space">bar code</div>
    </section>
  </div>
</div>
</body>
</html>
```